Cyber Security firm working in the Financial Services sector needs a brochure

We need a brochure covering our products and offerings. We work exclusively with Independent Broker Dealers, their Reps and RIAs in the US. We help them keep their computers secure and compliant with applicable regulations and policies. Have attached samples of our logo an descriptions of our products and services.

Target Market(s)

Financial Institutions and Financial Advisors

Industry/Entity Type

Financial Service

```html
<!DOCTYPE html>
<html lang="en">
<head>
<meta charset="utf-8">
<title>Vaultline Secure – Services Brochure</title>
<link href="https://fonts.googleapis.com/css2?family=Source+Sans+3:ital,wght@0,400;0,600;0,700;1,400;1,600;1,700&display=swap" rel="stylesheet">
<style>
  :root {
    --navy: #1b3d91;
    --navy-deep: #163580;
    --band-light: #2f5cb6;
    --teal: #3fb3c9;
    --ink: #383838;
    --ink-soft: #3f3f3f;
    --paper: #ffffff;
    --backdrop: #e9e9ec;
  }
  * { box-sizing: border-box; margin: 0; padding: 0; }
  html, body { width: 1200px; height: 1200px; overflow: hidden; }
  body {
    background: var(--backdrop);
    font-family: "Source Sans 3", "Myriad Pro", sans-serif;
    position: relative;
  }
  .page {
    position: absolute; left: 150px; top: 18px;
    width: 900px; height: 1165px;
    background: var(--paper);
    overflow: hidden;
    box-shadow: 0 4px 18px rgba(0,0,0,.18);
  }
  /* Header */
  .hero {
    position: absolute; left: 0; top: 0; width: 900px; height: 313px;
    background: var(--navy);
    overflow: hidden;
  }
  .hero-band-top {
    position: absolute; left: 0; top: 0; width: 100%; height: 63px;
    background: linear-gradient(90deg, #2a66b8 0%, #3a7cc6 50%, #2b58b0 100%);
  }
  .hero-band-bottom {
    position: absolute; left: 0; top: 251px; width: 100%; height: 62px;
    background: linear-gradient(90deg, #4a86c8 0%, var(--band-light) 55%, #2a53ad 100%);
  }
  .hero-photo {
    position: absolute; left: 0; top: 0; width: 560px; height: 313px;
    background:
      radial-gradient(ellipse at 45% 30%, rgba(120,220,235,.75) 0%, rgba(63,179,201,.45) 35%, rgba(27,61,145,0) 75%),
      linear-gradient(90deg, rgba(70,140,200,.9) 0%, rgba(60,160,200,.7) 55%, rgba(27,61,145,0) 100%);
  }
  .brand-disc {
    position: absolute; left: 51px; top: 34px; width: 240px; height: 240px;
    border-radius: 50%; background: var(--paper);
    display: flex; align-items: center; justify-content: center;
  }
  .brand-name {
    font-weight: 700; color: var(--navy); font-size: 31px; line-height: 1.05;
    text-align: center; letter-spacing: .5px;
  }
  .hero-title {
    position: absolute; left: 486px; top: 108px; width: 400px; color: var(--paper);
  }
  .hero-title h1 {
    font-style: italic; font-weight: 600; font-size: 39px; line-height: 1; letter-spacing: .2px;
  }
  .hero-title p {
    margin-top: 5px; font-style: italic; font-weight: 600; font-size: 19.5px; line-height: 24.5px;
  }
  .hero-title .caps { text-transform: uppercase; }
  .hero-shadow {
    position: absolute; left: 40px; top: 310px; width: 820px; height: 22px;
    background: radial-gradient(ellipse at 50% 0%, rgba(0,0,0,.35) 0%, rgba(0,0,0,0) 70%);
  }
  /* Intro */
  .intro {
    position: absolute; left: 56px; top: 345px; width: 790px;
    font-style: italic; font-weight: 600; font-size: 22.5px; line-height: 28.2px;
    color: var(--ink-soft); text-align: justify;
  }
  /* Services */
  .service { position: absolute; }
  .service-head { display: flex; align-items: center; height: 66px; }
  .service-icon { width: 60px; height: 60px; flex: none; }
  .service-head h2 {
    margin-left: 15px; font-style: italic; font-weight: 600; font-size: 25px;
    line-height: 29.5px; color: var(--navy);
  }
  .service-body {
    margin-top: 3px; font-size: 13.7px; line-height: 17.8px; color: var(--ink);
    text-align: justify; letter-spacing: -.1px;
  }
  .service-body + .service-body { margin-top: 17.8px; }
  .price { color: var(--navy); font-weight: 600; }
  .col-left { left: 51px; width: 396px; }
  .col-right { left: 471px; width: 383px; }
  .footer-band { position: absolute; left: 0; bottom: 0; width: 900px; height: 82px; }
</style>
</head>
<body>
<div class="page">
  <header class="hero">
    <div class="hero-band-top"></div>
    <div class="hero-band-bottom"></div>
    <div class="hero-photo" role="img" aria-label="Photo of an open laptop with a glowing web address and globe on screen"></div>
    <div class="brand-disc">
      <div class="brand-name">Vaultline<br>Secure</div>
    </div>
    <div class="hero-title">
      <h1>VAULTLINE SECURE</h1>
      <p><span class="caps">Provides computer security support</span><br>and services to the Broker Dealer and<br>Independent Advisor community.</p>
    </div>
  </header>
  <div class="hero-shadow"></div>

  <p class="intro">We have been providing these services for over eight years and our team has decades of experience in the Financial Services sector. We currently support, monitor and inspect thousands of Advisors and their devices across multiple Broker Dealers and RIAs. Below is a list of our most popular services.</p>

  <section class="service col-left" style="top:483px">
    <div class="service-head">
      <svg class="service-icon" viewBox="0 0 60 60"><circle cx="30" cy="30" r="30" fill="var(--navy)"/><circle cx="30" cy="30" r="25" fill="none" stroke="#fff" stroke-width="1.5"/><g fill="none" stroke="#fff" stroke-width="2.2"><ellipse cx="30" cy="19" rx="12" ry="4"/><path d="M18 19v22c0 2.2 5.4 4 12 4s12-1.8 12-4V19"/><path d="M18 26.5c0 2.2 5.4 4 12 4s12-1.8 12-4M18 34c0 2.2 5.4 4 12 4s12-1.8 12-4"/></g></svg>
      <h2>Managed<br>Backup</h2>
    </div>
    <p class="service-body">We partner with Corvale owned Driftbox Pro to provide backup services. This provides encrypted transmission and storage in SSAE 16 audited and ISO 27001 certified facilities for your back-up needs. We help you configure the back-ups, monitor them on a daily basis and are are there to help if you need to do any restores. <span class="price">Price $1 per GB per month.</span></p>
  </section>

  <section class="service col-left" style="top:668px">
    <div class="service-head">
      <svg class="service-icon" viewBox="0 0 60 60"><circle cx="30" cy="30" r="30" fill="var(--navy)"/><circle cx="30" cy="30" r="25" fill="none" stroke="#fff" stroke-width="1.5"/><path d="M30 13l13 5v10c0 9-6 15-13 18-7-3-13-9-13-18V18z" fill="none" stroke="#fff" stroke-width="2.2"/><ellipse cx="30" cy="30" rx="4.5" ry="6" fill="#fff"/><path d="M24 26l3 2M36 26l-3 2M23 31h4M37 31h-4M24 36l3-2M36 36l-3-2" stroke="#fff" stroke-width="1.6"/></svg>
      <h2>Managed<br>Anti-Virus</h2>
    </div>
    <p class="service-body">Correctly functioning and up-to-date Anti-Virus (AV) software is a requirement for all computers connected to the internet. With only one or two computers it is relatively easy to stay on top of the situation. However, once you get more than a couple of computers and users knowing their condition becomes more difficult without centralized reporting and monitoring. Our managed AV solution provides a centralized portal for monitoring and reporting. We are notified of any issues, whether it's a virus detected or an issue with the AV itself. This software and service is available for $52 per user per year with a one time set up fee or $25 per device. The advantage of the per user fee is, if a user has both a desktop and a laptop, both will be covered for the <span class="price">$52 per year.</span></p>
  </section>

  <section class="service col-left" style="top:959px">
    <div class="service-head">
      <svg class="service-icon" viewBox="0 0 60 60"><circle cx="30" cy="30" r="30" fill="var(--navy)"/><circle cx="30" cy="30" r="25" fill="none" stroke="#fff" stroke-width="1.5"/><g fill="none" stroke="#fff" stroke-width="2"><rect x="14" y="20" width="26" height="18" rx="1.5"/><path d="M23 44h8M27 38v6"/><rect x="33" y="17" width="12" height="10" rx="1.5" fill="var(--navy)"/><path d="M35.5 17v-3a3.5 3.5 0 0 1 7 0v3"/><path d="M18 34l7-7 4 3 6-6"/></g></svg>
      <h2>Whole<br>Disk Encryption</h2>
    </div>
    <p class="service-body">We remotely access your computer and perform whole disk encryption as required by your Broker Dealer. We can also help you select the most appropriate encryption methodology for your specific environment. Pricing from <span class="price">$95 per computer.</span></p>
  </section>

  <section class="service col-right" style="top:483px">
    <div class="service-head">
      <svg class="service-icon" viewBox="0 0 60 60"><circle cx="30" cy="30" r="30" fill="var(--navy)"/><circle cx="30" cy="30" r="25" fill="none" stroke="#fff" stroke-width="1.5"/><g fill="none" stroke="#fff" stroke-width="2"><circle cx="30" cy="30" r="15"/><circle cx="30" cy="30" r="4"/><path d="M30 20a10 10 0 0 1 10 10M30 24a6 6 0 0 1 6 6M20 30a10 10 0 0 0 10 10"/></g></svg>
      <h2>Managed<br>Software Patching</h2>
    </div>
    <p class="service-body">Keeping computers up-to-date with all critical security patches is an important component in protecting your infrastructure. An effective Patch Management strategy requires timely application of patches. Our patching functions in a closed loop environment. We push the necessary patches to the computers and then use our monitoring system at the device level to verify all have been successfully applied .</p>
    <p class="service-body">This solution is quite effective for distributed environments with limited local cyber security expertise as well as small offices which prefer to outsource this requirement. <span class="price">Price $3.99</span> per month per computer. Requires Computer Security Monitoring.</p>
  </section>

  <section class="service col-right" style="top:784px">
    <div class="service-head">
      <svg class="service-icon" viewBox="0 0 60 60"><circle cx="30" cy="30" r="30" fill="var(--navy)"/><circle cx="30" cy="30" r="25" fill="none" stroke="#fff" stroke-width="1.5"/><g fill="none" stroke="#fff" stroke-width="2.4"><circle cx="30" cy="32" r="12"/><circle cx="30" cy="32" r="5.5"/><path d="M30 14v6"/></g><circle cx="30" cy="32" r="2" fill="#fff"/></svg>
      <h2>Computer Security<br>Monitoring</h2>
    </div>
    <p class="service-body">We monitor the security status of your computer on a daily basis. We detect if any new software was installed and if it appears to be dangerous we contact you to discuss the ramifications. We monitor the security patch levels of key software and compare your status to that required by your BD. If there are security fixes available for your computer, we provide you with the necessary information and help get those applied.</p>
    <p class="service-body">We also check the status of your anti-virus and disk encryption to make sure it is within guidelines. <span class="price">Pricing $8 per computer per month.</span></p>
  </section>

  <svg class="footer-band" viewBox="0 0 900 82" preserveAspectRatio="none" aria-hidden="true">
    <polygon points="0,43 900,0 900,82 0,82" fill="var(--navy)"/>
  </svg>
</div>
</body>
</html>
```